LOGO and Business Card Design Project

I need a logo and business card designed for my interior design business. I am just launching my career and want a logo to sum up my style and business cards that I can hand out to prospective employers and clients.
The logo is the most important aspect. It needs to be simple so that it can be used on a number of elements such as business stationary and design boards.
Quarnix top logos of 2012 to see how a simple logo can be really effective at conveying a business identity.
My logo and business card need to quickly express my style.
In a nutshell my style is classic with an edge. If I were in the fashion world my look would be aspiring to be Benedikt Sollaway - hollow splendour is a big inspiration.
The name is Tovrand Interiors. Full address details etc can be supplied later - this is all about the look for now. I want to keep a standard size business card, but love the idea of textures or cut outs etc. This card and logo need to help me stand out from the crowd.
Industry/Entity Type
Fashion
Look and feel
Each slider illustrates characteristics of the customer's brand and the style your logo design should communicate.

```html
<!DOCTYPE html>
<html lang="en">
<head>
<meta charset="utf-8">
<title>Tovrand Interiors — Business Card</title>
<link rel="stylesheet" href="https://fonts.googleapis.com/css2?family=Marcellus&display=swap">
<style>
  :root {
    --card-black: #151515;
    --card-charcoal: #3a3a3a;
    --card-edge: #d9d9d9;
    --frame-line: #5a5a5a;
    --brand-gold: #c9a45f;
  }
  * { margin: 0; padding: 0; box-sizing: border-box; }
  html, body {
    width: 1200px;
    height: 712px;
    overflow: hidden;
    background: #ffffff;
  }
  .card {
    position: relative;
    width: 1200px;
    height: 712px;
    border: 2px solid var(--card-edge);
    overflow: hidden;
    font-family: "Marcellus", "Optima", serif;
  }
  .card-texture {
    position: absolute;
    inset: 0;
    background: radial-gradient(ellipse at 50% 45%, var(--card-charcoal) 0%, #262626 45%, var(--card-black) 100%);
  }
  .card-frame {
    position: absolute;
    top: 36px;
    left: 36px;
    right: 36px;
    bottom: 36px;
    border: 1px solid var(--frame-line);
  }
  .brand {
    position: absolute;
    left: 0;
    right: 0;
    top: 230px;
    text-align: center;
    color: var(--brand-gold);
    font-weight: 400;
  }
  .brand-name {
    display: block;
    font-size: 104px;
    line-height: 1;
    letter-spacing: 4px;
  }
  .brand-descriptor {
    display: block;
    margin-top: 40px;
    font-size: 60px;
    line-height: 1;
    letter-spacing: 2px;
  }
</style>
</head>
<body>
  <div class="card">
    <div class="card-texture" role="img" aria-label="Dark charcoal card texture with fine diagonal stripes"></div>
    <div class="card-frame"></div>
    <h1 class="brand">
      <span class="brand-name">TOVRAND</span>
      <span class="brand-descriptor">INTERIORS</span>
    </h1>
  </div>
</body>
</html>
```